Selling High quality Eco-windows. brisklatch.co.uk

I need a logo and website to market and sell high quality triple glazed windows and Tervola Mark certified windows. These windows can be supply only or supply and fit. They are very energy efficient with low U Values. They are made of timber not PVC or metal. I already run a small Eco-building outfit, completing roofing jobs and renovations with attention to quality detailing, energy conservation and renewable energy systems. I am inspired by Scandinavian simplicity and modern architecture. I am a keen environmentalist.

Target Market(s)

Environmentally aware home owners. Wealthier holiday home owners. Eco house projects. Energy efficient renovations.

Industry/Entity Type

Construction

Number of Pages Required

1 page

Font styles to use
Sans Serif

Colors
2fb6a2
ede9f3
3277b5

Requirements
Must have
• Great images. Eco feel but not 'rustic'. Bold and modern but not 'Tall gables'.
• Affordable. Message: "They will save you energy in the long run. Why loose heat through poor quality glazing? These windows will pay for themselves over time in lower energy bills"
• Optimized for tablets and smart phones.
Nice to have
• Scandinavian inspired. Real wood and not plastic.
• See documents below for existing images and colours.
Should not have
• Should not look, earthy, hippy or rustic. But also not incredibly flash Tall Gables style. These windows are affordable to the average person but great quality. They will add value to any building.

```html
<!DOCTYPE html>
<html lang="en">
<head>
<meta charset="utf-8">
<title>Brisklatch – Triple Glazed Timber Windows</title>
<link rel="stylesheet" href="https://fonts.googleapis.com/css2?family=Raleway:wght@400;500;600&family=Open+Sans:wght@400;600;700&display=swap">
<style>
:root{
  --teal:#2fb6a2;
  --blue:#3277b5;
  --pale:#ede9f3;
  --ink:#1d1d1d;
  --text:#6b6b6b;
  --white:#ffffff;
  --rule:#d4d0dc;
}
*{box-sizing:border-box;margin:0;padding:0}
html,body{width:1200px;height:2459px;overflow:hidden}
body{position:relative;background:var(--white);font-family:"Open Sans",Arial,sans-serif;color:var(--text)}
.abs{position:absolute}
.heading{font-family:"Raleway",Arial,sans-serif}
.accent{color:var(--teal)}
.btn{position:absolute;background:var(--blue);color:var(--white);font-size:13px;font-weight:600;display:flex;align-items:center;justify-content:center;text-transform:uppercase;text-decoration:none}

/* header */
.site-header{left:0;top:0;width:1200px;height:95px;background:var(--white)}
.brand{left:46px;top:16px;display:flex;align-items:center;gap:12px}
.brand-mark{width:62px;height:62px;border:3px solid var(--teal);border-radius:50%}
.brand-name{font-family:"Raleway",Arial,sans-serif;font-size:36px;font-weight:500;color:var(--blue);letter-spacing:1px}
.main-nav{right:50px;top:0;height:95px;display:flex}
.main-nav a{display:flex;align-items:center;padding:0 24px;font-size:11px;font-weight:600;color:var(--ink);text-decoration:none;text-transform:uppercase}
.main-nav a.active{background:var(--blue);color:var(--white);padding:0 17px}

/* hero */
.hero{left:0;top:95px;width:1200px;height:565px;background:linear-gradient(100deg,#6a6158 0%,#8c7a5a 30%,#5a554f 60%,#3a3633 100%)}
.hero-shade{left:0;top:95px;width:1200px;height:565px;background:rgba(0,0,0,.25)}
.hero-title{left:49px;top:284px;font-size:70px;font-weight:500;color:var(--white);letter-spacing:1px}
.hero-text{left:50px;top:376px;width:620px;font-size:14px;font-weight:600;line-height:21px;color:var(--white)}
.slider-dots{display:flex;gap:9px}
.slider-dots span{width:14px;height:14px;border-radius:50%;background:var(--white)}
.slider-dots span.on{background:var(--teal)}

/* feature band */
.feature-band{left:0;top:660px;width:1200px;height:274px;background:rgba(40,40,40,.92);border-top:4px solid var(--white)}
.feature{width:300px;text-align:center}
.feature-photo{position:absolute;width:170px;height:170px;border-radius:50%;border:4px solid var(--white)}
.feature-title{font-size:15px;font-weight:500;color:var(--teal)}
.feature-text{width:240px;margin:8px auto 0;font-size:12px;line-height:17px;color:#9a9a9a}
.feature-more{margin-top:10px;font-size:12px;font-weight:700;color:var(--white)}

/* welcome */
.welcome-title{left:48px;top:972px;font-size:30px;font-weight:500;color:var(--ink)}
.welcome-text{left:48px;top:1031px;width:680px;font-size:12.4px;line-height:20.5px}
.welcome-photo{left:795px;top:982px;width:356px;height:203px;background:linear-gradient(135deg,#e6e6e6,#b9bcbd 55%,#c8a98a)}

/* triple band */
.triple-band{left:0;top:1259px;width:1200px;height:380px;background:linear-gradient(180deg,#3b3a35,#4a3f30 45%,#2e2d2a)}
.triple-title{left:0;top:1372px;width:1200px;text-align:center;font-size:60px;font-weight:400;color:var(--white)}
.triple-text{left:160px;top:1470px;width:880px;text-align:center;font-size:14px;line-height:23px;color:var(--white)}

/* testimonials */
.testimonials-title{left:0;top:1688px;width:1200px;text-align:center;font-size:29px;font-weight:500;color:var(--ink)}
.quote-mark{font-family:"Raleway",Arial,sans-serif;font-size:60px;font-weight:600;color:var(--teal);line-height:1}
.testimonial-card{left:130px;top:1787px;width:917px;height:147px;border:1px solid #d6d6d6;border-radius:4px;box-shadow:0 1px 4px rgba(0,0,0,.08)}
.avatar{left:165px;top:1809px;width:112px;height:112px;border-radius:50%;border:3px solid #d6d6d6;background:linear-gradient(180deg,#cfd3d8,#7b8593)}
.testimonial-text{left:302px;top:1826px;width:700px;font-size:14px;line-height:21px}
.testimonial-name{right:208px;top:1897px;font-size:18px;font-weight:700;color:var(--teal)}
.ring-dots{display:flex;gap:6px}
.ring-dots span{width:12px;height:12px;border-radius:50%;border:1.5px solid var(--teal)}
.ring-dots span.on{background:var(--teal)}

/* footer */
.site-footer{left:0;top:2065px;width:1200px;height:274px;background:var(--pale)}
.footer-divider{top:2090px;width:1px;height:230px;background:var(--rule)}
.footer-heading{font-family:"Raleway",Arial,sans-serif;font-size:17px;font-weight:600;color:var(--teal);text-transform:uppercase}
.footer-text{font-size:12px;line-height:17px;color:#555}
.email-field{left:522px;top:2212px;width:297px;height:36px;background:var(--white);font-size:11px;color:#aaa;padding:10px 12px}
.contact-list{left:945px;top:2155px;width:230px;font-size:12px;line-height:17px;color:#555}
.contact-list li{list-style:none;display:flex;gap:14px;margin-bottom:6px}
.contact-list svg{flex:none;margin-top:3px}

.bottom-bar{left:0;top:2339px;width:1200px;height:120px;background:var(--blue)}
.legal-links{left:0;top:2360px;width:1200px;text-align:center;font-size:11px;font-weight:600;color:var(--white)}
.social{top:2396px;width:34px;height:34px;border-radius:50%;border:1.5px solid var(--white)}
</style>
</head>
<body>

<header class="abs site-header">
  <div class="abs brand"><span class="brand-mark"></span><span class="brand-name">BRISKLATCH</span></div>
  <nav class="abs main-nav">
    <a class="active" href="#">Home</a><a href="#">About Us</a><a href="#">Our Product</a><a href="#">Gallery</a><a href="#">Testimonials</a><a href="#">Contact</a>
  </nav>
</header>

<section>
  <div class="abs hero" role="img" aria-label="Cut-away samples of timber triple glazed window frames in a showroom"></div>
  <div class="abs hero-shade"></div>
  <h1 class="abs heading hero-title">BRISKLATCH</h1>
  <p class="abs hero-text">Lorem ipsum dolor sit amet, consectetur adipiscing elit, sed do eiusmod tempor incididunt ut labore et dolore magna aliqua. Ut enim ad minim veniam</p>
  <a class="btn" style="left:49px;top:438px;width:131px;height:44px">Read More</a>
  <div class="abs slider-dots" style="left:59px;top:613px"><span class="on"></span><span></span><span></span></div>
</section>

<section class="abs feature-band"></section>
<div class="abs feature-photo" role="img" aria-label="Close-up of a triple glazed window corner" style="left:335px;top:590px;background:linear-gradient(135deg,#c9b38c,#8f8777 50%,#d8d4cc)"></div>
<div class="abs feature-photo" role="img" aria-label="Timber window frame profile section" style="left:792px;top:590px;background:linear-gradient(135deg,#f0d2b5,#d59c74 55%,#e9c6a6)"></div>
<div class="abs feature" style="left:270px;top:783px">
  <h3 class="heading feature-title">Triple Glazed Windows</h3>
  <p class="feature-text">Lorem ipsum dolor sit amet, consectetur ipsum dolor sit amet, consectetur adipis do edit</p>
  <p class="feature-more">MORE &#9656;</p>
</div>
<div class="abs feature" style="left:727px;top:783px">
  <h3 class="heading feature-title">Tervola Mark Certified Windows</h3>
  <p class="feature-text">Lorem ipsum dolor sit amet, consectetur ipsum dolor sit amet, consectetur adipis do edit</p>
  <p class="feature-more">MORE &#9656;</p>
</div>

<section>
  <h2 class="abs heading welcome-title">WELCOME TO <span class="accent">BRISKLATCH</span></h2>
  <p class="abs welcome-text">We make high quality eco windows from real timber, never PVC or metal. Our triple glazed and Tervola Mark certified windows have very low U values and are offered supply only or supply and fit. Inspired by Scandinavian simplicity and modern architecture, each frame is detailed with care for energy conservation. They are affordable for the average home owner, suit renovations, holiday homes and eco house projects alike, and will add lasting value to any building. They will save you energy in the long run.</p>
  <a class="btn" style="left:46px;top:1159px;width:113px;height:38px">Read More</a>
  <div class="abs welcome-photo" role="img" aria-label="Cross-section of an aluminium-clad timber window frame"></div>
</section>

<section>
  <div class="abs triple-band" role="img" aria-label="Timber-framed glazed building facade at dusk"></div>
  <h2 class="abs heading triple-title">TRIPLE GLAZED WINDOWS</h2>
  <p class="abs triple-text">They will save you energy in the long run. Why lose heat through poor quality glazing? These windows will pay for themselves over time in lower energy bills, with low U values and warm real timber frames.</p>
</section>

<section>
  <h2 class="abs heading testimonials-title">OUR <span class="accent">TESTIMONIALS</span></h2>
  <span class="abs quote-mark" style="left:133px;top:1742px">&ldquo;</span>
  <div class="abs testimonial-card"></div>
  <div class="abs avatar" role="img" aria-label="Portrait of the customer"></div>
  <p class="abs testimonial-text">Lorem ipsum dolor sit amet, consectetur adipiscing elit, sed do eiusmod tempor incididunt ut labore et dolore magna aliqua. Ut enim ad minim veniam, quis nostrud exercitation ullamco laboris nisi ut aliquip ex ea commodo consequat.</p>
  <p class="abs testimonial-name">- Elin Marsh</p>
  <span class="abs quote-mark" style="left:1018px;top:1955px">&rdquo;</span>
  <div class="abs ring-dots" style="left:578px;top:1995px"><span></span><span class="on"></span><span></span></div>
</section>

<footer>
  <div class="abs site-footer"></div>
  <div class="abs footer-divider" style="left:467px"></div>
  <div class="abs footer-divider" style="left:885px"></div>

  <h4 class="abs footer-heading" style="left:57px;top:2104px">About Us</h4>
  <p class="abs footer-text" style="left:51px;top:2145px;width:365px">Lorem ipsum dolor sit amet, consectetur adipiscing elit, sed do eiusmod tempor incididunt ut labore et dolore magna aliqua. Ut enim ad minim veniam, quis nostrud exercitation ullamco laboris nisi ut aliquip ex ea commodo consequat. Duis aute irure dolor in reprehenderit in voluptate velit esse cillum dolore eu fugiat nulla pariatur.</p>
  <a class="btn" style="left:51px;top:2278px;width:126px;height:38px;font-size:11px">Read More</a>

  <h4 class="abs footer-heading" style="left:522px;top:2104px">Newsletter Signup</h4>
  <p class="abs footer-text" style="left:522px;top:2146px;width:310px">Subscribe our newsletter to know our daily updates and offer daily updates and offerpsun dolor sit amet elit, sed aliqua.</p>
  <div class="abs email-field">Enter your Email Id</div>
  <a class="btn" style="left:522px;top:2260px;width:297px;height:36px;font-size:14px">Subscribe</a>

  <h4 class="abs footer-heading" style="left:945px;top:2104px">Location</h4>
  <ul class="abs contact-list">
    <li><svg width="10" height="13" viewBox="0 0 10 13"><path d="M5 0a5 5 0 0 0-5 5c0 4 5 8 5 8s5-4 5-8a5 5 0 0 0-5-5zm0 7a2 2 0 1 1 0-4 2 2 0 0 1 0 4z" fill="#2fb6a2"/></svg><span>Company Name<br>Address Line 1, Address Line 2<br>Country - 123456</span></li>
    <li><svg width="11" height="11" viewBox="0 0 11 11"><path d="M2 0l2 2.5-1.2 1.4a7 7 0 0 0 3.3 3.3L7.5 6 10 8 8.5 10.5C4 10 .5 6.5 0 2z" fill="#2fb6a2"/></svg><span>Office: (206) 555-0142</span></li>
    <li><svg width="11" height="9" viewBox="0 0 11 9"><rect width="11" height="9" fill="#2fb6a2"/><path d="M0 0l5.5 4.5L11 0" stroke="#fff" fill="none"/></svg><span>hello@brisklatch.co.uk</span></li>
  </ul>

  <div class="abs bottom-bar"></div>
  <p class="abs legal-links">About Us &nbsp;/&nbsp; Privacy Policy &nbsp;/&nbsp; Terms of Service &nbsp;/&nbsp; Contact Us</p>
  <span class="abs social" style="left:498px"></span>
  <span class="abs social" style="left:543px"></span>
  <span class="abs social" style="left:588px"></span>
  <span class="abs social" style="left:633px"></span>
  <span class="abs social" style="left:678px"></span>
</footer>

</body>
</html>
```